Bref créative
Business cards, stationery, powerpoint template, and email signature for business consulting firm
Bellwether Advisory Group The Ground Level Method
Simple
Corwin Pike
Consultant
PO Box 7086
Austell, GA 30497
cpike@bellwethgrp.net
We will be adding new employees so I would like the business card file to be changeable. I would like to see both one sided and two-sided business cards.
The logo files will have all parts of the logo available both separate and complete.
This is the complete logo
This is the file with the logo components

```html
<!DOCTYPE html>
<html lang="en">
<head>
<meta charset="utf-8">
<title>Bellwether Advisory Group – Business Card</title>
<link href="https://fonts.googleapis.com/css2?family=Cinzel:wght@400;600&family=Cormorant+Garamond:wght@500;600&display=swap" rel="stylesheet">
<style>
  :root {
    --backdrop: #d9d9db;
    --card: #ffffff;
    --purple: #4b2a82;
    --purple-light: #6a46a8;
    --black: #111111;
    --ink: #3a3a3a;
    --grey: #8a8a8a;
    --orange: #e79a1c;
  }
  html, body {
    margin: 0;
    width: 1200px;
    height: 987px;
    overflow: hidden;
    background: var(--backdrop);
  }
  .canvas {
    position: relative;
    width: 1200px;
    height: 987px;
  }
  .card {
    position: absolute;
    left: 220px;
    width: 760px;
    height: 420px;
    background: var(--card);
    border-radius: 26px;
    overflow: hidden;
    box-shadow: 0 10px 28px rgba(0,0,0,0.18);
  }
  .card-front { top: 50px; }
  .card-back { top: 517px; }

  /* Front */
  .front-mark {
    position: absolute;
    inset: 0;
    display: flex;
    align-items: center;
    justify-content: center;
    gap: 16px;
  }
  .mark-dot {
    width: 30px;
    height: 30px;
    border-radius: 50%;
    background: var(--orange);
  }
  .brand-name {
    font-family: "Cinzel", serif;
    font-weight: 600;
    color: var(--purple);
    letter-spacing: 1px;
  }
  .front-mark .brand-name { font-size: 30px; }

  /* Back */
  .back-brand {
    position: absolute;
    left: 40px;
    top: 44px;
  }
  .back-brand-row {
    display: flex;
    align-items: center;
    gap: 14px;
  }
  .back-brand .mark-dot { width: 36px; height: 36px; }
  .back-brand .brand-name { font-size: 32px; }
  .tagline {
    margin: 6px 0 0 50px;
    font-family: "Cormorant Garamond", serif;
    font-weight: 600;
    font-size: 13px;
    letter-spacing: 3px;
    text-transform: uppercase;
    color: var(--grey);
  }
  .contact-list {
    position: absolute;
    left: 40px;
    top: 150px;
    margin: 0;
    padding: 0;
    list-style: none;
    font-family: "Cormorant Garamond", serif;
    font-weight: 500;
    font-size: 17px;
    color: var(--ink);
  }
  .contact-list li {
    display: flex;
    align-items: center;
    gap: 10px;
    height: 24px;
  }
  .contact-icon {
    width: 14px;
    height: 14px;
    flex: none;
  }
  .person {
    position: absolute;
    right: 44px;
    top: 284px;
    text-align: left;
  }
  .person-name {
    font-family: "Cinzel", serif;
    font-weight: 600;
    font-size: 22px;
    color: var(--purple);
  }
  .person-title {
    font-family: "Cormorant Garamond", serif;
    font-weight: 500;
    font-size: 15px;
    color: var(--ink);
    margin-top: 2px;
  }
  .bottom-band {
    position: absolute;
    left: 0;
    bottom: 0;
    width: 760px;
    height: 110px;
  }
  .web-strip {
    position: absolute;
    right: 44px;
    bottom: 12px;
    font-family: "Cormorant Garamond", serif;
    font-size: 12px;
    letter-spacing: 3px;
    color: #cfcfcf;
    text-transform: uppercase;
  }
</style>
</head>
<body>
<main class="canvas">

  <section class="card card-front" aria-label="Business card front">
    <div class="front-mark">
      <span class="mark-dot"></span>
      <span class="brand-name">Bellwether Advisory Group</span>
    </div>
  </section>

  <section class="card card-back" aria-label="Business card back">
    <div class="back-brand">
      <div class="back-brand-row">
        <span class="mark-dot"></span>
        <span class="brand-name">Bellwether Advisory Group</span>
      </div>
      <p class="tagline">The Ground Level Method</p>
    </div>

    <ul class="contact-list">
      <li>
        <svg class="contact-icon" viewBox="0 0 14 14"><circle cx="7" cy="7" r="7" fill="var(--purple)"/><path d="M7 3.2a2.4 2.4 0 0 0-2.4 2.4c0 1.8 2.4 4.8 2.4 4.8s2.4-3 2.4-4.8A2.4 2.4 0 0 0 7 3.2z" fill="#fff"/></svg>
        PO Box 7086 Dunmore Falls
      </li>
      <li>
        <svg class="contact-icon" viewBox="0 0 14 14"><circle cx="7" cy="7" r="7" fill="var(--purple)"/><path d="M7 3.2a2.4 2.4 0 0 0-2.4 2.4c0 1.8 2.4 4.8 2.4 4.8s2.4-3 2.4-4.8A2.4 2.4 0 0 0 7 3.2z" fill="#fff"/></svg>
        TN 38521
      </li>
      <li>
        <svg class="contact-icon" viewBox="0 0 14 14"><circle cx="7" cy="7" r="7" fill="var(--purple)"/><path d="M4.6 3.6l1.4-.3.8 1.9-.9.7a5 5 0 0 0 2.2 2.2l.7-.9 1.9.8-.3 1.4c-3.3.2-6-2.5-5.8-5.8z" fill="#fff"/></svg>
        770.555.0143
      </li>
      <li>
        <svg class="contact-icon" viewBox="0 0 14 14"><circle cx="7" cy="7" r="7" fill="var(--purple)"/><rect x="3.6" y="4.6" width="6.8" height="4.8" fill="#fff"/><path d="M3.6 4.6L7 7.4l3.4-2.8" fill="none" stroke="var(--purple)" stroke-width=".8"/></svg>
        cpike@bellwethgrp.net
      </li>
      <li>
        <svg class="contact-icon" viewBox="0 0 14 14"><circle cx="7" cy="7" r="7" fill="var(--purple)"/><circle cx="7" cy="7" r="3.3" fill="none" stroke="#fff" stroke-width=".9"/><path d="M3.7 7h6.6M7 3.7c-1.6 2-1.6 4.6 0 6.6M7 3.7c1.6 2 1.6 4.6 0 6.6" fill="none" stroke="#fff" stroke-width=".7"/></svg>
        www.bellwethgrp.net
      </li>
    </ul>

    <div class="person">
      <div class="person-name">Corwin Pike</div>
      <div class="person-title">Consultant</div>
    </div>

    <svg class="bottom-band" viewBox="0 0 760 110" preserveAspectRatio="none" aria-hidden="true">
      <defs>
        <linearGradient id="bandPurple" x1="0" y1="0" x2="1" y2="0">
          <stop offset="0" stop-color="var(--purple)"/>
          <stop offset="1" stop-color="var(--purple-light)"/>
        </linearGradient>
      </defs>
      <path d="M0 30 H300 C318 30 322 66 340 66 H760 V110 H0 Z" fill="url(#bandPurple)"/>
      <path d="M0 48 H310 C326 48 330 76 346 76 H760 V110 H0 Z" fill="var(--black)"/>
      <path d="M0 30 H300 C318 30 322 66 340 66 H760" fill="none" stroke="#ffffff" stroke-opacity=".35" stroke-width="1"/>
    </svg>
    <div class="web-strip">www.bellwethgrp.net</div>
  </section>

</main>
</body>
</html>
```